Collectibles expert needs a new business card design.

My current business card makes me look to high end. It may even make me look arrogant or too stuffy. I do work with high end clients and their items but most of my business is with average people with average items. My business name is Walter Brennick's Oak Lane Digging Co. The idea was that I mine the streets helping people discover the treasures buried in their homes. That could be art, jewelry, coins, etc. The name and an older logo I used does not make immediate sense to most people. I tried to go with just my picture and name and that is the current card I am changing. I help people who need to downsize. Whether they are getting rid of one item, a collection or a house full of items I help them discover what they have, what it is worth and what are the best ways we can get the most for them. This may be a combination of estate sale (which I dont do) auction or sell directly to a dealer or collector. Usually it is a combination of these. My main goal is to help make sure they dont accidently sell a Vantorre painting in a garage sale. I am uploading a copy of my old card and the old logo I used to use but the winning card design will need to be much different than these. You can learn a little more about me at www.walterpbrennick.com, www.oaklanedigin.com and www.facebook.com/oldco. I hope someone can look at what I do and come up with a very unique design that will be equally effective if my client is high income or if my client is low to mid income. I do not care if it is a one or two sided card as long as it conveys my contact information and a good representation of what I do.

Target Market(s)

People who are getting rid of items. These can be elderly couples or individuals that are moving to an active living community and will have less space so they need to sell items. This can also include the children of elder parents that dont want their stuff and want to find solutions to help them get rid of their items.

Contact Information for Business Card

The card should have my business name Walter Brennick's Oak Lane Digging Co., phone number 555-382-19073, email walter@oaklanedigging.com and website www.oaklanedigging.com. Would also like to include Buyer, Broker, Consultant and Appraiser. We can put Walter P. Brennick, ISA on the opposite side of the company name since it includes my name as well.

Font styles to use
Sans Serif

Colors

Designer to choose colors to be used in the design.

Requirements
Must have
• My project must have a professional look. It must not alienate low income clients and should still be appealing to high value clients.

```html
<!DOCTYPE html>
<html lang="en">
<head>
<meta charset="utf-8">
<title>Walter Brennick's Oak Lane Digging Co. — Business Card</title>
<link href="https://fonts.googleapis.com/css2?family=Oswald:wght@500;700&family=Lato:wght@400;700&display=swap" rel="stylesheet">
<style>
  :root {
    --slate: #58585a;
    --slate-dark: #4a4a4c;
    --gold: #9c7a2e;
    --paper: #f4f4f4;
    --ink: #4d4d4f;
    --backdrop: #e6e3de;
  }
  * { margin: 0; padding: 0; box-sizing: border-box; }
  html, body {
    width: 1200px; height: 900px; overflow: hidden;
    background: var(--backdrop);
  }
  .canvas { position: relative; width: 1200px; height: 900px; }

  .card {
    position: absolute;
    width: 560px; height: 320px;
    overflow: hidden;
    box-shadow: 0 10px 28px rgba(0,0,0,0.22);
  }

  /* Front side */
  .card--front {
    left: 110px; top: 120px;
    background: var(--slate);
    display: flex; flex-direction: column; align-items: center; justify-content: center;
    color: #fff;
  }
  .brand-mark {
    width: 110px; height: 110px;
    border: 10px solid #fff; border-radius: 50%;
    margin-bottom: 26px;
  }
  .brand-name {
    font-family: 'Oswald', sans-serif; font-weight: 700;
    text-align: center; text-transform: none; line-height: 1.1;
    color: #fff;
  }
  .brand-name__owner { display: block; font-size: 22px; }
  .brand-name__company { display: block; font-size: 32px; text-transform: uppercase; letter-spacing: 0.5px; }

  /* Back side */
  .card--back {
    left: 530px; top: 440px;
    background: var(--paper);
  }
  .card__wave { position: absolute; inset: 0; }
  .person {
    position: absolute; left: 46px; top: 64px;
  }
  .person__name {
    font-family: 'Oswald', sans-serif; font-weight: 500;
    font-size: 22px; color: var(--ink); text-transform: uppercase; letter-spacing: 0.3px;
  }
  .person__roles {
    font-family: 'Lato', sans-serif; font-size: 15px; color: var(--ink); margin-top: 2px;
  }
  .back-brand {
    position: absolute; right: 34px; top: 40px; width: 130px;
    display: flex; flex-direction: column; align-items: center; gap: 8px;
  }
  .back-brand__mark {
    width: 62px; height: 62px; border-radius: 50%; background: var(--gold);
  }
  .back-brand__name {
    font-family: 'Oswald', sans-serif; font-weight: 500;
    font-size: 13px; line-height: 1.2; color: var(--slate); text-align: center;
  }
  .contact {
    position: absolute; left: 46px; top: 186px;
    list-style: none;
    font-family: 'Lato', sans-serif; font-size: 15px; color: var(--ink);
  }
  .contact__item { display: flex; align-items: center; gap: 8px; height: 22px; }
  .contact__icon { width: 13px; height: 13px; fill: var(--ink); flex: none; }
</style>
</head>
<body>
<main class="canvas">

  <section class="card card--front" aria-label="Business card front">
    <div class="brand-mark" aria-hidden="true"></div>
    <h1 class="brand-name">
      <span class="brand-name__owner">Walter Brennick's</span>
      <span class="brand-name__company">Oak Lane Digging Co.,</span>
    </h1>
  </section>

  <section class="card card--back" aria-label="Business card back">
    <svg class="card__wave" viewBox="0 0 560 320" preserveAspectRatio="none" aria-hidden="true">
      <path d="M0 300 C160 296 360 236 560 122 L560 138 C360 252 170 306 0 316 Z" fill="var(--gold)"/>
      <path d="M0 322 C170 312 360 262 560 146 L560 320 L0 320 Z" fill="var(--slate)"/>
    </svg>

    <div class="person">
      <h2 class="person__name">Walter P. Brennick, ISA</h2>
      <p class="person__roles">Buyer, Broker, Consultant and Appraiser</p>
    </div>

    <div class="back-brand">
      <div class="back-brand__mark" aria-hidden="true"></div>
      <p class="back-brand__name">Walter Brennick's<br>Oak Lane Digging Co.</p>
    </div>

    <ul class="contact">
      <li class="contact__item">
        <svg class="contact__icon" viewBox="0 0 16 16" aria-hidden="true"><path d="M3 1h3l1.5 4-2 1.3a9 9 0 0 0 4.2 4.2L11 8.5l4 1.5v3c0 1-1 2-2 2C6.5 15 1 9.5 1 3c0-1 1-2 2-2z"/></svg>
        <span>555-382-19073</span>
      </li>
      <li class="contact__item">
        <svg class="contact__icon" viewBox="0 0 16 16" aria-hidden="true"><path d="M1 3h14v10H1z M1 3l7 6 7-6" fill="none" stroke="var(--ink)" stroke-width="1.6"/></svg>
        <span>walter@oaklanedigging.com</span>
      </li>
      <li class="contact__item">
        <svg class="contact__icon" viewBox="0 0 16 16" aria-hidden="true"><circle cx="8" cy="8" r="7"/></svg>
        <span>www.oaklanedigging.com</span>
      </li>
    </ul>
  </section>

</main>
</body>
</html>
```